Business Card Design

Melodrift Podcast

Industry/Entity Type

Business

Contact Information for Business Card

YOU ARE INVITED TO LISTEN
Stretch Your Mindset
Award Winning Melodrift Podcast
with Dr. Maren Holloway
www.drmarenholloway.example

555-781-3096

```html
<!DOCTYPE html>
<html lang="en">
<head>
<meta charset="utf-8">
<title>Melodrift Podcast – Business Card</title>
<link rel="stylesheet" href="https://fonts.googleapis.com/css2?family=Carlito:wght@400;700&family=Open+Sans:wght@700&display=swap">
<style>
  :root {
    --page-bg: #4a4a4a;
    --card-light: #cde68a;
    --card-mid: #b3d862;
    --card-edge: #9cc647;
    --band-dark: #1f4a0c;
    --band-mid: #3f7a1c;
    --wave-silver: #d8dcd6;
    --ink: #161616;
    --ink-light: #ffffff;
    --icon-green: #2f6f2a;
    --mic-light: #e6e8e6;
    --mic-dark: #5a5c5c;
  }
  * { margin: 0; padding: 0; box-sizing: border-box; }
  html, body { width: 1200px; height: 820px; overflow: hidden; }
  body { background: var(--page-bg); position: relative; font-family: "Carlito", "Calibri", sans-serif; }

  .business-card {
    position: absolute;
    left: 364px; top: 275px;
    width: 472px; height: 270px;
    overflow: hidden;
    background: radial-gradient(ellipse at 35% 35%, var(--card-light) 0%, var(--card-mid) 60%, var(--card-edge) 100%);
  }

  .mic-photo {
    position: absolute;
    left: 300px; top: 26px;
    width: 168px; height: 244px;
    border-radius: 70px 70px 20px 20px;
    background: linear-gradient(90deg, var(--mic-dark) 0%, var(--mic-light) 45%, var(--mic-dark) 100%);
  }

  .bottom-band { position: absolute; left: 0; bottom: 0; width: 472px; height: 50px; }

  .card-text { position: absolute; left: 16px; top: 26px; }

  .headline {
    font-family: "Open Sans", "Arial", sans-serif;
    font-weight: 700;
    font-size: 18.5px;
    color: var(--ink);
    letter-spacing: 0.1px;
    line-height: 24px;
  }
  .tagline {
    margin-top: 7px;
    width: 270px;
    font-size: 12.5px;
    line-height: 15px;
    color: var(--ink-light);
  }
  .host-name {
    margin-top: 26px;
    font-size: 21px;
    color: var(--ink-light);
    line-height: 26px;
  }
  .contact-list { margin-top: 12px; list-style: none; }
  .contact-item {
    display: flex; align-items: center;
    font-size: 17px; line-height: 25px; color: var(--ink);
  }
  .contact-icon { width: 13px; height: 13px; margin-right: 7px; flex: none; }
</style>
</head>
<body>
  <div class="business-card">
    <div class="mic-photo" role="img" aria-label="Photo of a vintage chrome studio microphone"></div>

    <svg class="bottom-band" viewBox="0 0 472 50" aria-hidden="true">
      <defs>
        <linearGradient id="band-fill" x1="0" y1="0" x2="0" y2="1">
          <stop offset="0" stop-color="var(--band-mid)"/>
          <stop offset="1" stop-color="var(--band-dark)"/>
        </linearGradient>
      </defs>
      <path d="M0 22 C 80 8, 200 6, 300 16 S 430 26, 472 18 L 472 50 L 0 50 Z" fill="url(#band-fill)"/>
      <path d="M0 22 C 80 8, 200 6, 300 16 S 430 26, 472 18" fill="none" stroke="var(--wave-silver)" stroke-width="3"/>
    </svg>

    <div class="card-text">
      <h1 class="headline">YOU ARE INVITED TO LISTEN</h1>
      <p class="tagline">Stretch Your Mindset Award Winning Melodrift Podcast with :</p>
      <p class="host-name">Dr. Maren Holloway</p>
      <ul class="contact-list">
        <li class="contact-item">
          <svg class="contact-icon" viewBox="0 0 14 14" aria-hidden="true">
            <circle cx="7" cy="7" r="6.2" fill="none" stroke="var(--icon-green)" stroke-width="1.3"/>
            <path d="M4.6 3.8 L5.8 3.6 L6.4 5.3 L5.6 6 Q6.3 7.6 8 8.4 L8.7 7.6 L10.4 8.2 L10.2 9.4 Q9.6 10.2 8.6 10 Q5 8.9 4 5.4 Q3.8 4.4 4.6 3.8 Z" fill="var(--icon-green)"/>
          </svg>
          <span>555-781-3096</span>
        </li>
        <li class="contact-item">
          <svg class="contact-icon" viewBox="0 0 14 14" aria-hidden="true">
            <circle cx="7" cy="7" r="6.2" fill="none" stroke="var(--icon-green)" stroke-width="1.3"/>
            <path d="M3.5 5 Q5.5 4 6.5 5.5 Q7 7 8.5 7.5 Q9 9.5 7.5 11 M8 3.2 Q9.5 4.2 10.5 4" fill="none" stroke="var(--icon-green)" stroke-width="1.3"/>
          </svg>
          <span>www.drmarenholloway.example</span>
        </li>
      </ul>
    </div>
  </div>
</body>
</html>
```